The Velvet Heron Business Card

Looking for new business cards for our Directors and Manager
I have attached what they are currently, they are also gold foiled where you see gold sections. We do want them to be quite special and exciting being a show venue.
Please use Lanternshowhouse logo for Dean Morcup and Kaye Lindahl, please use Velvet Heron Marqueeland for Jed Quall and Martin Gabe

https://files.examplevault.net/f/7QpLwX2mRtz9KbVnYc4HsD8gJe3UaFo?mode=view_link

I need 3 different versions for Directors and Managers.
Card One:
Dean Morcup
Director of The Velvet Heron Lanternshowhouse
0492 647 258
dean@quellary.com.au
velvetheronshows.com

Card Two:
Martin Gabe
Director of The Velvet Heron Marqueeland
0463 921 574
martin@vhmq.com.au
velvetheronshows.com

Card Three:
Jed Quall
Venue Manager of The Velvet Heron Marqueeland
0447 286 190
qldoperations@vhmq.com.au
velvetheronshows.com

Card Four:

Kaye Lindahl
0428 364 917
kaye@skyhoopers.com.au
velvetheronshows.com

Logo:
https://files.examplevault.net/f/9HtRwq4ZmNb2XcLpVe6YdKs8FjA3uTg

Colour Scheme: Hot Pink and Baby Pink
Gold Accents

We want something different but as inspiration, I have attached the current card. The gold part was foiled. Standard business card sizes.

```html
<!DOCTYPE html>
<html lang="en">
<head>
<meta charset="utf-8">
<title>The Velvet Heron – Business Card</title>
<link href="https://fonts.googleapis.com/css2?family=Montserrat:wght@400;500;600;700&display=swap" rel="stylesheet">
<style>
  :root {
    --backdrop: #b9b9b9;
    --card-white: #fbf7f9;
    --baby-pink: #f3c9dc;
    --wash-pink: #e9a5c4;
    --hot-pink: #c2368a;
    --ink: #2a2a2a;
    --logo-dark: #1a1114;
  }
  * { margin: 0; padding: 0; box-sizing: border-box; }
  html, body {
    width: 1000px;
    height: 1200px;
    overflow: hidden;
    background: var(--backdrop);
    font-family: "Montserrat", sans-serif;
  }
  .card {
    position: absolute;
    left: 117px;
    width: 766px;
    height: 438px;
    overflow: hidden;
    background: var(--card-white);
  }
  .card--front { top: 102px; }
  .card--back { top: 620px; }

  .card__wash {
    position: absolute;
    inset: 0;
    background:
      radial-gradient(ellipse 70% 55% at 20% 85%, var(--wash-pink) 0%, rgba(233,165,196,0) 70%),
      radial-gradient(ellipse 60% 50% at 85% 90%, var(--baby-pink) 0%, rgba(243,201,220,0) 75%),
      radial-gradient(ellipse 50% 40% at 10% 15%, var(--baby-pink) 0%, rgba(243,201,220,0) 70%),
      linear-gradient(180deg, #fdf9fb 0%, #f8e3ec 60%, #f1c3d8 100%);
  }

  .brand {
    position: absolute;
    display: flex;
    flex-direction: column;
    align-items: center;
    transform: translateX(-50%);
  }
  .brand__dot {
    border-radius: 50%;
    background: var(--logo-dark);
  }
  .brand__name {
    font-weight: 700;
    color: var(--hot-pink);
    white-space: nowrap;
    letter-spacing: 0.02em;
  }
  .card--front .brand { left: 383px; top: 70px; }
  .card--front .brand__dot { width: 150px; height: 150px; }
  .card--front .brand__name { font-size: 62px; margin-top: 16px; }

  .card--back .brand { left: 182px; top: 140px; }
  .card--back .brand__dot { width: 90px; height: 90px; }
  .card--back .brand__name { font-size: 31px; margin-top: 10px; }

  .divider {
    position: absolute;
    left: 368px;
    top: 95px;
    width: 2px;
    height: 251px;
    background: var(--hot-pink);
  }
  .contact {
    position: absolute;
    left: 406px;
    top: 126px;
    color: var(--ink);
  }
  .contact__name {
    font-size: 27px;
    font-weight: 600;
    color: var(--hot-pink);
    letter-spacing: 0.01em;
  }
  .contact__role {
    margin-top: 8px;
    font-size: 13px;
    font-weight: 500;
    line-height: 1.35;
  }
  .contact__details {
    list-style: none;
    margin-top: 40px;
    font-size: 17.5px;
    line-height: 26px;
  }
</style>
</head>
<body>
  <section class="card card--front">
    <div class="card__wash" role="img" aria-label="Soft pink watercolour wash background"></div>
    <div class="brand">
      <span class="brand__dot"></span>
      <span class="brand__name">The Velvet Heron</span>
    </div>
  </section>

  <section class="card card--back">
    <div class="card__wash" role="img" aria-label="Soft pink watercolour wash background"></div>
    <div class="brand">
      <span class="brand__dot"></span>
      <span class="brand__name">The Velvet Heron</span>
    </div>
    <span class="divider"></span>
    <div class="contact">
      <h1 class="contact__name">DEAN MORCUP</h1>
      <p class="contact__role">Director of The Velvet Heron<br>Lanternshowhouse</p>
      <ul class="contact__details">
        <li>0492 647 258</li>
        <li>dean@quellary.com.au</li>
        <li>velvetheronshows.com</li>
      </ul>
    </div>
  </section>
</body>
</html>
```